Local Healthy meal delivery service needs a new flyer

Looking for a fresh and modern flyer design for a company called "Brindlecove Fare Works". We provide healthy and delicious meals to families, business offices and health care workers. We would like to see designs that communicate freshness, convenience, non contact delivery and customizable meal plan options. We would like to see designs that mirror our website colors, look and feel: brindlecovefareworks.com

Target Market(s)

Families, Business Offices, Health care workers

Requirements
Must have
• Color scheme and layout matching our brand and website
Our Logo
Modern clean/professional look
contact info: website, phone number, social media
Appropriate photos
Nice to have
• "How it Works" Summary

```html
<!DOCTYPE html>
<html lang="en">
<head>
<meta charset="utf-8">
<title>Brindlecove Fare Works – Meal Delivery Flyer</title>
<link rel="stylesheet" href="https://fonts.googleapis.com/css2?family=Oswald:wght@400;500;600;700&family=Montserrat:wght@400;600;800&display=swap">
<style>
:root{
  --green:#1b7d1b;
  --green-deep:#157015;
  --olive:#6e9a2a;
  --olive-dark:#4a5c21;
  --ink:#1d1d1d;
  --paper:#ffffff;
  --stage:#5a5a5a;
  --line:#2a8a2a;
}
*{margin:0;padding:0;box-sizing:border-box}
html,body{width:999px;height:1200px;overflow:hidden;background:var(--stage)}
.flyer{position:absolute;left:35px;top:0;width:928px;height:1200px;background:var(--paper);overflow:hidden;font-family:'Montserrat',sans-serif;color:var(--ink)}
.art{position:absolute;left:0;top:0}
.abs{position:absolute}
.cond{font-family:'Oswald',sans-serif}

.brand{left:40px;top:120px;width:270px;display:flex;align-items:center;gap:10px}
.brand-dot{width:22px;height:22px;border-radius:50%;background:var(--green);flex:none}
.brand-name{font-family:'Oswald',sans-serif;font-weight:600;font-size:25px;line-height:1.05;color:var(--green);letter-spacing:.5px}

.hero-title{left:30px;width:415px;top:372px;text-align:center;color:#fff;font-family:'Oswald',sans-serif;font-weight:400;font-size:49px;line-height:1;letter-spacing:-.5px}
.hero-sub{left:90px;top:431px;width:303px;height:32px;background:#fff;color:var(--green);font-family:'Oswald',sans-serif;font-size:20px;display:flex;align-items:center;justify-content:center}
.hero-rule{left:169px;top:480px;width:146px;height:1px;background:rgba(255,255,255,.6)}
.order{left:30px;width:415px;top:490px;text-align:center;color:#fff;font-family:'Oswald',sans-serif;font-weight:600;font-size:26px;letter-spacing:9px}
.url{left:87px;top:527px;width:309px;height:34px;background:#fff;color:#222;font-family:'Oswald',sans-serif;font-size:18px;letter-spacing:1.6px;display:flex;align-items:center;justify-content:center}
.url b{font-weight:600}
.delivery{left:30px;width:415px;top:566px;text-align:center;color:#fff;font-family:'Oswald',sans-serif;font-weight:400;font-size:35px;line-height:37px}
.delivery b{font-weight:700}
.locations{left:30px;width:415px;top:652px;text-align:center;color:#fff;font-family:'Oswald',sans-serif;font-size:15.5px;letter-spacing:.6px}

.bar{position:absolute;width:2px;background:var(--green)}
.h-green{color:var(--green)}
.h-olive{color:var(--olive)}
.heading{font-family:'Oswald',sans-serif;font-weight:700;font-size:29px;line-height:36px;letter-spacing:-.2px}
.howto-tag{left:72px;top:860px;width:206px;height:34px;background:var(--olive);color:#fff;font-family:'Oswald',sans-serif;font-size:24px;padding-left:20px;line-height:34px;clip-path:polygon(0 0,84% 0,100% 100%,0 100%)}
.copy{font-size:13.8px;line-height:21px;color:var(--ink)}
.options{font-family:'Oswald',sans-serif;font-size:20px;color:var(--ink)}

.audience{left:0;width:928px;top:1026px;text-align:center;font-family:'Oswald',sans-serif;font-size:19.5px;color:var(--ink);letter-spacing:-.2px}
.audience b{color:var(--green);font-weight:700}

.values{left:56px;top:1068px;width:816px;height:52px;background:var(--olive-dark);border-radius:4px;display:flex;align-items:center;justify-content:space-evenly;color:#fff;font-family:'Oswald',sans-serif;font-size:27px;z-index:2}
.values .sep{width:1px;height:26px;background:rgba(255,255,255,.7)}

.phone{left:56px;top:1130px;height:56px;display:flex;align-items:center;gap:12px;color:#fff;font-family:'Montserrat',sans-serif;font-weight:800;font-size:44px;letter-spacing:.5px}
.contact{left:487px;top:1146px;display:flex;align-items:center;gap:10px;color:#fff;font-size:16px}
.contact .div{width:1px;height:18px;background:#fff;margin:0 4px}
.social{width:21px;height:21px;border-radius:50%;background:#fff;opacity:.9}
</style>
</head>
<body>
<main class="flyer">
  <svg class="art" width="928" height="1200" viewBox="0 0 928 1200">
    <defs>
      <clipPath id="heroClip"><circle cx="680" cy="205" r="345"/></clipPath>
      <linearGradient id="heroFood" x1="0" y1="0" x2="1" y2="1">
        <stop offset="0" stop-color="#8a6a4a"/>
        <stop offset=".45" stop-color="#d9d3c6"/>
        <stop offset="1" stop-color="#6f8a3a"/>
      </linearGradient>
      <radialGradient id="greenDisc" cx=".5" cy=".45" r=".6">
        <stop offset="0" stop-color="#1f8a1f"/>
        <stop offset="1" stop-color="#146914"/>
      </radialGradient>
    </defs>
    <!-- hero photo area -->
    <circle cx="680" cy="205" r="352" fill="none" stroke="#9cc48a" stroke-width="1"/>
    <rect x="0" y="0" width="928" height="560" fill="url(#heroFood)" clip-path="url(#heroClip)" role="img" aria-label="Photo: grilled chicken salad with tomatoes and greens on a white plate with fork and spoon, glass of lemon water on a wooden table"/>
    <!-- green offer disc -->
    <circle cx="237" cy="510" r="222" fill="url(#greenDisc)"/>
    <circle cx="237" cy="510" r="210" fill="none" stroke="rgba(255,255,255,.7)" stroke-width="1"/>
    <!-- small bowl photo -->
    <circle cx="527" cy="563" r="103" fill="#fff" stroke="var(--line)" stroke-width="1.2"/>
    <circle cx="527" cy="563" r="97" fill="#9fb86a" role="img" aria-label="Photo: bowl of quinoa with avocado, broccoli, cucumber and carrot"/>
    <!-- large meal prep photo -->
    <circle cx="762" cy="583" r="160" fill="#fff" stroke="var(--line)" stroke-width="1.2"/>
    <circle cx="762" cy="583" r="153" fill="#5d7a30" role="img" aria-label="Photo: meal prep container with sliced roasted chicken, spinach and brussels sprouts"/>
    <!-- bottom contact band -->
    <rect x="0" y="1098" width="928" height="102" fill="var(--olive)"/>
    <polygon points="0,1098 460,1098 428,1200 0,1200" fill="var(--green)"/>
  </svg>

  <div class="abs brand"><span class="brand-dot"></span><span class="brand-name">BRINDLECOVE<br>FARE WORKS</span></div>

  <div class="abs hero-title">FRESH &amp; FIT MEAL</div>
  <div class="abs hero-sub">DELIVERY FRESHLY PREPARED MEAL</div>
  <div class="abs hero-rule"></div>
  <div class="abs order">ORDER ONLINE</div>
  <div class="abs url">www.<b>brindlecovefareworks</b>.com</div>
  <div class="abs delivery">FOR <b>HOME DELIVERY</b><br>OR <b>PICK UP</b></div>
  <div class="abs locations">AT OUR PREFERRED DELIVERY LOCATIONS</div>

  <section>
    <span class="bar" style="left:53px;top:776px;height:63px"></span>
    <h2 class="abs heading" style="left:71px;top:772px"><span class="h-green">WE PROVIDE FRESH,</span><br><span class="h-olive">FULLY COOKED, READY TO EAT MEALS!</span></h2>
    <div class="abs howto-tag">HOW IT WORKS</div>
    <p class="abs copy" style="left:72px;top:914px;width:395px">Every Tuesday we publish 2 menus for the following week, one for each delivery day (Tuesday &amp; Thursday). Place order by Midnight on Saturday with meal plan and delivery location.</p>
  </section>

  <section>
    <span class="bar" style="left:524px;top:776px;height:28px"></span>
    <h2 class="abs heading" style="left:540px;top:772px"><span class="h-green">MEAL PREP</span> <span class="h-olive">DELIVERED!</span></h2>
    <p class="abs copy" style="left:540px;top:814px;width:340px;font-size:13px;line-height:19px">We drop off a blue soft cooler with your name on it to your specified delivery location on the day you choose. Leave your empty cooler at the drop off location and we replace it with a fresh one on your next order.</p>
    <span class="bar" style="left:524px;top:936px;height:62px"></span>
    <h2 class="abs heading" style="left:540px;top:933px"><span class="h-green">HEALTHY</span> <span class="h-olive">LIFESTYLE</span></h2>
    <p class="abs options" style="left:540px;top:970px"><span class="h-olive">Gluten Free</span> and <span class="h-olive">Vegetarian</span> Options Available</p>
  </section>

  <p class="abs audience"><b>WE PROVIDE</b> HEALTHY AND DELICIOUS MEALS TO <b>FAMILIES, BUSINESS OFFICES AND HEALTH CARE WORKERS</b></p>

  <div class="abs values">
    <span>LOCAL</span><span class="sep"></span><span>FRESH</span><span class="sep"></span><span>ALL NATURAL</span><span class="sep"></span><span>NON-GMO</span><span class="sep"></span><span>NO ANTIBIOTICS</span>
  </div>

  <div class="abs phone">
    <svg width="42" height="42" viewBox="0 0 42 42" aria-hidden="true">
      <circle cx="21" cy="21" r="19" fill="none" stroke="#fff" stroke-width="2.5"/>
      <path d="M14 11c1.5-1 3-.5 3.6.6l1.6 3c.5 1-.1 2-.9 2.6l-1 .8c.8 2.6 2.8 4.8 5.4 5.8l.9-1c.7-.8 1.7-1.2 2.6-.7l3 1.7c1 .6 1.4 2.1.5 3.5-1.2 1.8-3.3 2.6-5.3 1.9C18.600 27.800 13.800 23 12.100 17.300c-.6-2.200.3-4.900 1.900-6.300z" fill="#fff"/>
    </svg>
    555-014-2298
  </div>
  <div class="abs contact">
    <svg width="16" height="12" viewBox="0 0 16 12" aria-hidden="true"><rect x=".75" y=".75" width="14.5" height="10.5" fill="none" stroke="#fff" stroke-width="1.3"/><path d="M1 1l7 6 7-6" fill="none" stroke="#fff" stroke-width="1.3"/></svg>
    <span>hello@brindlecovefareworks.com</span>
    <span class="div"></span>
    <span class="social" aria-label="Social profile"></span>
    <span class="social" aria-label="Social profile"></span>
  </div>
</main>
</body>
</html>
```